Medical Prescription for Diagnostic Sleep Testing

Tamber Ridge Vital Labs main marketing tool is our Prescription that we leave with medical providers. Prescription is printed on 8.5 x 11 sheets of paper to create a prescription pad for our medical providers. Prescription should fit to one page. Tamber Ridge Vital Labs works with 250 different medical providers so it is important we are able to update and change the medical provider information at bottom. The medical provider would fill-out top with patient information, check-off center testing and patient co-morbidity and Fax to Tamber Ridge Vital Labs. Because it is Faxed to us it is important to have clear print and large font Attached or uploaded file is one example we currently use. Please review all 5 must haves.

Target Market(s)

Prescription for medical providers to fill-out and fax to Tamber Ridge Vital Labs to conduct the sleep study.

Industry/Entity Type

Medical

Colors

Designer to choose only greyscale colors for use in the design.

Requirements
Must have
• 1) Prescription Size: 8.5 x 11
• 2) Must fit to One page Only
• 3) Ability to change medical provider information at bottom of prescription. We work with 250 different medical providers
• 4) Ability to change or update any part of prescription
• 5) Document Must be created in Microsoft Word 2016. This is the program we use for our prescriptions.
Nice to have
• Can be done in Gray-Scale or Black and White since its being faxed from the medical provider to us.

```html
<!DOCTYPE html>
<html lang="en">
<head>
<meta charset="utf-8">
<title>Sleep Study Physician Order</title>
<link href="https://fonts.googleapis.com/css2?family=Caladea:wght@400;700&family=Roboto+Condensed:wght@400&family=Tinos&display=swap" rel="stylesheet">
<style>
:root{
  --ink:#000000;
  --heading:#111111;
  --muted:#2b2b2b;
  --line:#000000;
  --badge:#8c8c8c;
  --paper:#ffffff;
}
*{box-sizing:border-box;margin:0;padding:0}
html,body{width:974px;height:1200px;overflow:hidden;background:var(--paper)}
body{position:relative;font-family:"Caladea",serif;color:var(--ink)}
.abs{position:absolute;white-space:nowrap}
.brand{left:42px;top:16px;width:205px;height:124px;border:2px solid var(--heading);border-radius:10px;display:flex;flex-direction:column;align-items:center;justify-content:center;gap:10px}
.brand-name{font-weight:700;font-size:21px;color:var(--heading);text-align:center;line-height:1.15;white-space:normal}
.badge{width:40px;height:18px;background:var(--badge);border-radius:2px}
.title{left:280px;width:670px;top:21px;text-align:center;font-weight:700;font-size:39px;color:var(--heading);line-height:1}
.phones{left:280px;width:670px;top:70px;text-align:center;font-weight:700;font-size:31px;line-height:1}
.address{left:280px;width:670px;top:102px;text-align:center;font-weight:700;font-size:18.5px;line-height:1.1}
.field{font-size:18.5px;line-height:1}
.blank{display:inline-block;border-bottom:1.5px solid var(--line);height:15px;vertical-align:baseline}
.small{font-size:10px}
.h2{left:58px;font-weight:700;font-size:29px;color:var(--heading);line-height:1}
.order{left:58px;width:880px;font-size:15.5px;line-height:19px;white-space:normal}
.rule{left:58px;width:880px;border-top:2.5px solid var(--line)}
.dash{left:58px;width:860px;border-top:1.5px dashed var(--line)}
.checks{left:62px;top:622px;display:grid;grid-template-columns:259px 225px 300px;font-size:19px;line-height:24.3px}
.check{display:flex;align-items:center;gap:10px;white-space:nowrap}
.box{display:inline-block;width:11px;height:11px;border:1.5px solid var(--ink);box-shadow:1.5px 1.5px 0 var(--ink);flex:none}
.clinic{left:58px;top:860px;font-family:"Roboto Condensed",sans-serif;font-size:29px;color:var(--heading);line-height:1}
.clinic-info{left:58px;top:893px;font-size:17px;color:var(--muted)}
.providers{left:62px;top:928px;display:grid;grid-template-columns:229px 232px 240px;row-gap:14px;font-size:16px;line-height:19px}
.provider{display:flex;gap:10px;white-space:nowrap}
.provider .box{margin-top:4px}
.npi{color:var(--muted)}
.sign{left:58px;top:1059px;font-size:19px;line-height:1}
.submit{left:58px;top:1084px;font-size:19.5px;line-height:1}
.attach{left:58px;top:1109px;font-family:"Tinos",serif;font-size:16px;display:flex;align-items:center;gap:5px;line-height:1}
.thanks{left:58px;top:1146px;font-family:"Roboto Condensed",sans-serif;font-size:29px;line-height:1}
</style>
</head>
<body>
<div class="abs brand">
  <div class="brand-name">Tamber Ridge<br>Vital Labs</div>
  <div class="badge" role="img" aria-label="Accreditation badge"></div>
</div>
<h1 class="abs title">Sleep Study Physician Order</h1>
<div class="abs phones">Phone: (555) 210-4418 &nbsp;•&nbsp; Fax: (555) 210-4419</div>
<div class="abs address">2480 W. Larkspur Avenue, Suite 3-C; Fairbrook, NV 89000</div>

<div class="abs field" style="left:58px;top:154px">Patient Name: <span class="blank" style="width:244px"></span></div>
<div class="abs field" style="left:433px;top:154px">DOB: <span class="blank" style="width:56px"></span>/<span class="blank" style="width:56px"></span>/<span class="blank" style="width:56px"></span></div>
<div class="abs field" style="left:670px;top:154px">Telephone: <span class="blank" style="width:106px"></span></div>

<div class="abs field" style="left:58px;top:194px">Alternate Telephone: <span class="blank" style="width:126px"></span></div>
<div class="abs field" style="left:364px;top:194px">Primary Insurance: <span class="blank" style="width:134px"></span></div>
<div class="abs field" style="left:658px;top:194px">Secondary: <span class="blank" style="width:140px"></span></div>

<div class="abs field" style="left:58px;top:234px">Insurance:<span class="blank" style="width:134px"></span></div>
<div class="abs field" style="left:304px;top:234px">Height:<span class="blank" style="width:60px"></span></div>
<div class="abs field" style="left:442px;top:234px">Weight:<span class="blank" style="width:100px"></span></div>
<div class="abs field" style="left:637px;top:234px">Patient Gender <span class="small">(circle one)</span>: &nbsp;M &nbsp;/ &nbsp;F</div>

<h2 class="abs h2" style="top:282px">Diagnostic Sleep Study Ordered</h2>
<p class="abs order" style="top:314px">• <b>COMPLETE SLEEP STUDY</b> : (Based on Insurance or Patient’s Choice)&nbsp; In-Lab Sleep Study (PSG) or Home Sleep Study (PSG 95810 / HST 95806) with follow-up PAP Titration Study (PAP 95811 if positive for sleep apnea)</p>
<p class="abs order" style="top:364px">• <b>PEDIATRIC SLEEP STUDY</b>: PSG w/End Tidal CO2 Monitoring (PSG 95782 under 6 years of age &amp; PSG 95810 older than 6 years of age)</p>
<p class="abs order" style="top:414px">• <b>In-Lab Diagnostic Sleep Study/Polysomnogram</b> (PSG 95810)</p>
<p class="abs order" style="top:447px">• <b>SPLIT-NIGHT STUDY</b> (PSG with PAP 95810 &amp; 95811) To Comply With Accreditation &amp;Insurance &nbsp;Guidelines: AHI must be 20 or greater with minimum 2 hour recorded sleep time and 3 hours minimum to complete PAP treatment.</p>
<p class="abs order" style="top:497px">• <b>CPAP/BiPAP/BiPAP ST Titration Study</b> (Patients with documented sleep apnea 95811)</p>
<p class="abs order" style="top:529px">• &nbsp;<b>Home Sleep Study</b> (HST 95806 Conducted in patient’s home &amp; unattended by technologist) (No insurance patient cost $250.00)</p>

<h2 class="abs h2" style="top:582px">Patient Medical Necessity – Please Check All Boxes That Apply</h2>
<div class="abs rule" style="top:611px"></div>
<div class="abs checks">
  <div class="check"><span class="box"></span>Atrial Fibrillation</div>
  <div class="check"><span class="box"></span>Bipolar Disorder</div>
  <div class="check"><span class="box"></span>Congestive Heart Failure</div>
  <div class="check"><span class="box"></span>COPD</div>
  <div class="check"><span class="box"></span>Depression</div>
  <div class="check"><span class="box"></span>Excessive Daytime Sleepiness</div>
  <div class="check"><span class="box"></span>Frequent Urination</div>
  <div class="check"><span class="box"></span>Heart Disease</div>
  <div class="check"><span class="box"></span>History Heart Attack</div>
  <div class="check"><span class="box"></span>Hypertension</div>
  <div class="check"><span class="box"></span>Insomnia</div>
  <div class="check"><span class="box"></span>Mental or Mood Disorder</div>
  <div class="check"><span class="box"></span>Loud Snoring</div>
  <div class="check"><span class="box"></span>Morbid Obesity</div>
  <div class="check"><span class="box"></span>Morning Headaches</div>
  <div class="check"><span class="box"></span>Narcolepsy</div>
  <div class="check"><span class="box"></span>Opioid Use</div>
  <div class="check"><span class="box"></span>PTSD</div>
  <div class="check"><span class="box"></span>Pulmonary Disease</div>
  <div class="check"><span class="box"></span>Restless Leg Syndrome</div>
  <div class="check"><span class="box"></span>Seizures</div>
  <div class="check"><span class="box"></span>Shift Work Sleep disorder</div>
  <div class="check"><span class="box"></span>Stroke / TIA</div>
  <div class="check"><span class="box"></span>Witnessed Apnea</div>
  <div class="check" style="grid-column:1 / 4;margin-top:2px"><span class="box"></span>Gasping Sensations with Frequent Awakenings</div>
</div>
<div class="abs dash" style="top:845px"></div>

<div class="abs clinic">Silverpine Ear + Sinus Clinic</div>
<div class="abs clinic-info">4175 N. Cedar Lane; Fairbrook, NV 89001-4410 &nbsp;•Telephone:&nbsp; 555-318-2290 &nbsp;&nbsp;Fax:&nbsp; 555-318-2291</div>
<div class="abs providers">
  <div class="provider"><span class="box"></span><div>Dr. Owen Mercer Hale<br><span class="npi">NPI: 1000000011</span></div></div>
  <div class="provider"><span class="box"></span><div>Dr. Glen R. Ashby<br><span class="npi">NPI: 1000000029</span></div></div>
  <div class="provider"><span class="box"></span><div>Dr Martin L. Breckow<br><span class="npi">NPI: 1000000037</span></div></div>
  <div class="provider"><span class="box"></span><div>Dr. Lena Park<br><span class="npi">NPI: 1000000045</span></div></div>
  <div class="provider"><span class="box"></span><div>Iris Delacourt, FNP-C<br><span class="npi">NPI: 1000000052</span></div></div>
  <div class="provider"><span class="box"></span><div>Neil Foster, PA-C<br><span class="npi">NPI: 1000000060</span></div></div>
</div>
<div class="abs rule" style="top:1033px"></div>

<div class="abs sign">Physician’s Signature:<span class="blank" style="width:135px"></span><span style="display:inline-block;width:32px"></span>Date: <span class="blank" style="width:50px"></span>/<span class="blank" style="width:50px"></span>/<span class="blank" style="width:50px"></span></div>
<div class="abs submit">Please Fax:555-210-4419 or Email:tamberridgelabs@example.com</div>
<div class="abs attach"><svg width="12" height="12" viewBox="0 0 11 11" aria-hidden="true"><rect x="0.5" y="0.5" width="10" height="10" fill="none" stroke="#000" stroke-width="1"/><path d="M2.5 5.5 L4.5 8 L9 2.5" fill="none" stroke="#000" stroke-width="1.3"/></svg> Fax Along With: Patient Demographic Information &nbsp;• &nbsp;Copy of Current Insurance Information &nbsp;• &nbsp;Clinical Notes</div>
<div class="abs thanks">Thank You For your support MARK &amp; LEO</div>
</body>
</html>
```